Business Card Design - Local Discount Club

Looking for a fun business card for a local discount club. One side should be the logo only and the other should be have :

Name
Title
Phone, Email
Website

```html
<!DOCTYPE html>
<html lang="en">
<head>
<meta charset="utf-8">
<title>The Harbor Bay Card – Business Card</title>
<link rel="stylesheet" href="https://fonts.googleapis.com/css2?family=Montserrat:wght@500;700&display=swap">
<style>
  :root{
    --backdrop:#c8c8ca;
    --navy:#1b2877;
    --navy-deep:#16216a;
    --sky:#3cbde9;
    --mint:#86e2b4;
    --brand-blue:#6d85e2;
    --text-soft:#c9d3f5;
    --map-tone:#22327f;
  }
  *{margin:0;padding:0;box-sizing:border-box}
  html,body{width:900px;height:1200px;overflow:hidden;background:var(--backdrop)}
  .canvas{position:relative;width:900px;height:1200px;font-family:"Montserrat",sans-serif}
  .card-art{position:absolute;inset:0}
  .card-shape{filter:drop-shadow(0 14px 14px rgba(0,0,0,.28))}
  .brand-name{position:absolute;left:314px;top:250px;width:400px;text-align:center;
    color:var(--brand-blue);font-weight:700;font-size:46px;line-height:1.15;
    letter-spacing:1px;text-transform:uppercase}
  .person{position:absolute;left:245px;top:780px;width:200px;text-align:right}
  .person-name{color:var(--sky);font-weight:700;font-size:19px;letter-spacing:.5px;white-space:nowrap}
  .person-title{color:var(--text-soft);font-weight:500;font-size:12px;margin-top:4px}
  .contact-list{position:absolute;left:468px;top:780px;list-style:none;color:var(--text-soft);font-size:12px;font-weight:500}
  .contact-list li{display:flex;align-items:center;gap:8px;height:19px;white-space:nowrap}
  .contact-list svg{width:11px;height:11px;flex:none}
</style>
</head>
<body>
<main class="canvas">
  <svg class="card-art" width="900" height="1200" viewBox="0 0 900 1200">
    <path class="card-shape card-front" fill="var(--navy-deep)"
      d="M330 128 L698 88 Q742 84 744 128 L746 470 Q746 522 700 524 L334 530 Q292 530 290 490 L282 332 Q280 300 292 268 Z"/>
    <circle class="brand-dot" cx="690" cy="150" r="13" fill="var(--sky)"/>

    <path class="card-shape card-back" fill="var(--navy)"
      d="M200 688 L596 688 Q610 688 620 698 L712 786 Q722 796 722 812 L722 1016 Q722 1034 704 1034 L192 1034 Q174 1034 174 1016 L174 706 Q174 688 200 688 Z"/>
    <rect role="img" aria-label="Faint map of the peninsula coastline" x="240" y="860" width="300" height="150" rx="60" fill="var(--map-tone)" opacity=".7"/>
    <circle class="accent-dot" cx="230" cy="712" r="12" fill="var(--sky)"/>
    <circle class="accent-dot" cx="262" cy="700" r="7" fill="var(--mint)"/>
  </svg>

  <p class="brand-name">The Harbor Bay<br>Card</p>

  <div class="person">
    <p class="person-name">DALE MORROW</p>
    <p class="person-title">Founder</p>
  </div>

  <ul class="contact-list">
    <li><svg viewBox="0 0 12 12"><path d="M2 1h3l1 3-1.5 1a6 6 0 0 0 2.5 2.5L8 6l3 1v3c0 1-1 1-1 1A9 9 0 0 1 1 2s0-1 1-1z" fill="var(--sky)"/></svg>555-204-7183</li>
    <li><svg viewBox="0 0 12 12"><rect x="1" y="2.5" width="10" height="7" rx="1" fill="var(--sky)"/><path d="M1.5 3l4.5 3.5L10.5 3" stroke="var(--navy)" fill="none"/></svg>hello@harborbaycard.com</li>
    <li><svg viewBox="0 0 12 12"><circle cx="6" cy="6" r="4.8" fill="none" stroke="var(--sky)" stroke-width="1.4"/><path d="M1.5 6h9M6 1.2c-2.5 3-2.5 6.6 0 9.6M6 1.2c2.5 3 2.5 6.6 0 9.6" stroke="var(--sky)" fill="none"/></svg>www.harborbaycard.com</li>
  </ul>
</main>
</body>
</html>
```